3D Animation for Screen on Entry Gate

We need 2 x 3D Animations for the entry screen that will sit on top of a turnstile as you enter a venue. These images need to be very clear, modern looking animated images.

1) The first animation will need to be a moving flashing or moving from small to large, Red Cross that also reads "Invalid"
2) The 2nd image needs to have the same look and feel but be a moving Green arrow - moving from the bottom of the screen to the top of the screen that also reads Access Granted

We will require the file to be provided as a mp4. thank you.

```html
<!DOCTYPE html>
<html lang="en">
<head>
<meta charset="utf-8">
<title>Entry Gate Screens</title>
<link rel="stylesheet" href="https://fonts.googleapis.com/css2?family=Archivo+Black&display=swap">
<style>
  :root {
    --page-bg: #000000;
    --granted-light: #4f8a26;
    --granted-mid: #2f5a16;
    --granted-dark: #1a330b;
    --ring-green-hi: #3fd13f;
    --ring-green: #139a13;
    --ring-green-dark: #063c06;
    --invalid-light: #d80000;
    --invalid-mid: #8a0000;
    --invalid-dark: #420000;
    --ring-red-hi: #ff4a4a;
    --ring-red: #c21010;
    --ring-red-dark: #3a0000;
    --face-top: #ffffff;
    --face-bottom: #cfcfcf;
    --depth-near: #9a9a9a;
    --depth-far: #4a4a4a;
    --edge: #6a6a6a;
  }
  html, body {
    margin: 0;
    padding: 0;
    width: 1200px;
    height: 1200px;
    overflow: hidden;
    background: var(--page-bg);
  }
  .gate-screens { display: block; width: 1200px; height: 1200px; }
  .status-word {
    font-family: "Archivo Black", "Arial Black", sans-serif;
    font-weight: 400;
  }
  .depth-far  { fill: var(--depth-far); }
  .depth-mid  { fill: #707070; }
  .depth-near { fill: var(--depth-near); }
  .face { fill: url(#face-shade); stroke: var(--edge); stroke-width: 1.5; paint-order: stroke; }
</style>
</head>
<body>
<svg class="gate-screens" viewBox="0 0 1200 1200" xmlns="http://www.w3.org/2000/svg">
  <defs>
    <radialGradient id="granted-glow" cx="0.55" cy="0.45" r="0.75">
      <stop offset="0" stop-color="var(--granted-light)"/>
      <stop offset="0.5" stop-color="var(--granted-mid)"/>
      <stop offset="1" stop-color="var(--granted-dark)"/>
    </radialGradient>
    <radialGradient id="invalid-glow" cx="0.58" cy="0.33" r="0.75">
      <stop offset="0" stop-color="var(--invalid-light)"/>
      <stop offset="0.45" stop-color="var(--invalid-mid)"/>
      <stop offset="1" stop-color="var(--invalid-dark)"/>
    </radialGradient>
    <linearGradient id="face-shade" x1="0" y1="0" x2="0" y2="1">
      <stop offset="0" stop-color="var(--face-top)"/>
      <stop offset="0.6" stop-color="#f1f1f1"/>
      <stop offset="1" stop-color="var(--face-bottom)"/>
    </linearGradient>
    <linearGradient id="ring-green-face" x1="0" y1="0" x2="1" y2="1">
      <stop offset="0" stop-color="var(--ring-green-hi)"/>
      <stop offset="0.5" stop-color="var(--ring-green)"/>
      <stop offset="1" stop-color="#0a6a0a"/>
    </linearGradient>
    <linearGradient id="ring-red-face" x1="0" y1="0" x2="1" y2="1">
      <stop offset="0" stop-color="var(--ring-red-hi)"/>
      <stop offset="0.5" stop-color="var(--ring-red)"/>
      <stop offset="1" stop-color="#7a0000"/>
    </linearGradient>

    <text id="word-access" class="status-word" x="476" y="332" font-size="116" textLength="484" lengthAdjust="spacingAndGlyphs">ACCESS</text>
    <text id="word-granted" class="status-word" x="480" y="444" font-size="116" textLength="552" lengthAdjust="spacingAndGlyphs">GRANTED</text>
    <text id="word-invalid" class="status-word" x="480" y="968" font-size="128" textLength="516" lengthAdjust="spacingAndGlyphs">INVALID</text>
    <path id="tick-shape" d="M312 324 L352 324 L408 394 L672 96 L408 438 Z"/>
    <path id="cross-shape" d="M-50 -88 L0 -38 L50 -88 L82 -56 L32 0 L82 56 L50 88 L0 38 L-50 88 L-82 56 L-32 0 L-82 -56 Z"/>
  </defs>

  <g class="screen screen--granted">
    <rect x="93" y="20" width="1016" height="572" fill="url(#granted-glow)"/>

    <g class="status-ring">
      <ellipse cx="406" cy="332" rx="110" ry="150" fill="none" stroke="var(--ring-green-dark)" stroke-width="26"/>
      <ellipse cx="400" cy="332" rx="110" ry="150" fill="none" stroke="#074a07" stroke-width="26"/>
      <ellipse cx="394" cy="332" rx="110" ry="150" fill="none" stroke="#0a5a0a" stroke-width="26"/>
      <ellipse cx="388" cy="332" rx="110" ry="150" fill="none" stroke="#0c680c" stroke-width="26"/>
      <ellipse cx="382" cy="332" rx="110" ry="150" fill="none" stroke="url(#ring-green-face)" stroke-width="26"/>
      <ellipse cx="382" cy="332" rx="98" ry="137" fill="none" stroke="var(--ring-green-hi)" stroke-width="2"/>
    </g>

    <g class="status-tick">
      <use href="#tick-shape" class="depth-far" transform="translate(8 -3)"/>
      <use href="#tick-shape" class="depth-mid" transform="translate(5 -2)"/>
      <use href="#tick-shape" class="depth-near" transform="translate(2 -1)"/>
      <use href="#tick-shape" class="face"/>
    </g>

    <g class="word-access">
      <use href="#word-access" class="depth-far" transform="translate(10 -4)"/>
      <use href="#word-access" class="depth-mid" transform="translate(7 -3)"/>
      <use href="#word-access" class="depth-mid" transform="translate(4 -2)"/>
      <use href="#word-access" class="depth-near" transform="translate(2 -1)"/>
      <use href="#word-access" class="face"/>
    </g>
    <g class="word-granted">
      <use href="#word-granted" class="depth-far" transform="translate(10 -4)"/>
      <use href="#word-granted" class="depth-mid" transform="translate(7 -3)"/>
      <use href="#word-granted" class="depth-mid" transform="translate(4 -2)"/>
      <use href="#word-granted" class="depth-near" transform="translate(2 -1)"/>
      <use href="#word-granted" class="face"/>
    </g>
  </g>

  <g class="screen screen--invalid">
    <rect x="93" y="600" width="1016" height="572" fill="url(#invalid-glow)"/>

    <g class="status-ring">
      <ellipse cx="412" cy="920" rx="118" ry="148" fill="var(--ring-red-dark)"/>
      <ellipse cx="404" cy="920" rx="118" ry="148" fill="none" stroke="#4a0000" stroke-width="24"/>
      <ellipse cx="396" cy="920" rx="118" ry="148" fill="none" stroke="#5e0000" stroke-width="24"/>
      <ellipse cx="388" cy="920" rx="118" ry="148" fill="none" stroke="#740000" stroke-width="24"/>
      <ellipse cx="380" cy="920" rx="118" ry="148" fill="#5a0000" stroke="url(#ring-red-face)" stroke-width="24"/>
      <ellipse cx="380" cy="920" rx="106" ry="136" fill="none" stroke="var(--ring-red-hi)" stroke-width="2"/>
    </g>

    <g class="status-cross" transform="translate(376 920)">
      <use href="#cross-shape" class="depth-far" transform="translate(9 -3)"/>
      <use href="#cross-shape" class="depth-mid" transform="translate(6 -2)"/>
      <use href="#cross-shape" class="depth-near" transform="translate(3 -1)"/>
      <use href="#cross-shape" class="face"/>
    </g>

    <g class="word-invalid">
      <use href="#word-invalid" class="depth-far" transform="translate(10 -4)"/>
      <use href="#word-invalid" class="depth-mid" transform="translate(7 -3)"/>
      <use href="#word-invalid" class="depth-mid" transform="translate(4 -2)"/>
      <use href="#word-invalid" class="depth-near" transform="translate(2 -1)"/>
      <use href="#word-invalid" class="face"/>
    </g>
  </g>
</svg>
</body>
</html>
```